Post Card Design Bright Lantern Youth

We need a postcard design that will be mailed to all residents offering free pickups of donated clothing. Our foundation is called Bright Lantern Youth, we are a nonprofit charitable organization that provides meals and medical services to children in need in Honduras. Collecting unwanted second-hand clothing generates revenue that helps fund the mission and programs run by our foundation. We would like to offer our pickup services to everyone who has any unwanted reusable clothing.

```html
<!DOCTYPE html>
<html lang="en">
<head>
<meta charset="utf-8">
<title>Bright Lantern Youth – Clothing Pickup Postcard</title>
<link href="https://fonts.googleapis.com/css2?family=Montserrat:wght@800;900&family=Oswald:wght@500;600;700&family=Roboto+Condensed:wght@400&display=swap" rel="stylesheet">
<style>
  :root {
    --paper: #f5f4ef;
    --page: #ffffff;
    --blue: #0095d9;
    --light-blue: #d6ecfa;
    --pink: #e8008a;
    --yellow: #ffe600;
    --gold: #fcc200;
    --green: #7cc02a;
    --orange: #f59a00;
    --ink: #1d1d1b;
    --white: #ffffff;
  }
  * { margin: 0; padding: 0; box-sizing: border-box; }
  html, body { width: 1200px; height: 1000px; overflow: hidden; background: var(--page); }
  .canvas { position: relative; width: 1200px; height: 1000px; }

  .postcard {
    position: absolute; left: 291px; width: 618px; height: 412px;
    background: var(--paper); overflow: hidden;
    font-family: "Roboto Condensed", "Arial Narrow", sans-serif;
  }
  .postcard--front { top: 73px; }
  .postcard--back { top: 527px; }

  .shape-layer { position: absolute; inset: 0; width: 618px; height: 412px; }

  /* Brand name */
  .brand-mark {
    position: absolute; display: flex; align-items: center; gap: 6px;
    font-family: "Oswald", sans-serif; font-weight: 600; color: var(--green);
    white-space: nowrap;
  }
  .brand-mark__dot { width: 12px; height: 12px; border-radius: 50%; background: var(--green); flex: none; }
  .postcard--front .brand-mark { left: 22px; top: 42px; font-size: 19px; }

  .hero-photo {
    position: absolute; left: 40px; top: 76px; width: 282px; height: 336px;
    background: radial-gradient(ellipse at 50% 35%, #e9c9a8 0%, #c9a27a 40%, #b28a62 70%, #8aa0b8 100%);
    border-radius: 140px 140px 0 0;
  }

  .headline-donate {
    position: absolute; right: 26px; top: 52px; text-align: right;
    font-family: "Montserrat", sans-serif; font-weight: 900; color: var(--yellow);
    font-size: 47px; line-height: 1; letter-spacing: -1px;
  }
  .headline-unwanted {
    position: absolute; right: 26px; top: 102px; text-align: right;
    font-family: "Montserrat", sans-serif; font-weight: 800; color: var(--white);
    font-size: 24px; line-height: 24px;
  }
  .headline-help {
    position: absolute; right: 26px; top: 172px; text-align: right;
    font-family: "Oswald", sans-serif; font-weight: 700; color: var(--yellow);
    font-size: 35px; line-height: 36px;
  }
  .front-copy {
    position: absolute; right: 26px; top: 265px; width: 185px; text-align: right;
    color: var(--white); font-size: 17px; line-height: 21.5px;
  }

  /* Back */
  .stamp-box {
    position: absolute; left: 484px; top: 33px; width: 99px; height: 101px;
    border: 1px dashed #555;
  }
  .address-line {
    position: absolute; left: 371px; width: 221px; border-top: 1px dashed #555;
  }
  .address-line--1 { top: 188px; }
  .address-line--2 { top: 233px; }
  .address-line--3 { top: 278px; }
  .back-title {
    position: absolute; left: 37px; top: 34px;
    font-family: "Oswald", sans-serif; font-weight: 600; color: var(--blue);
    font-size: 26px; line-height: 31px;
  }
  .back-copy {
    position: absolute; left: 37px; width: 330px; color: var(--ink);
    font-size: 11.6px; line-height: 14.2px;
  }
  .back-copy--intro { top: 97px; }
  .back-copy--impact { top: 161px; width: 260px; }
  .schedule-title {
    position: absolute; left: 37px; top: 199px;
    font-family: "Oswald", sans-serif; font-weight: 600; color: var(--pink);
    font-size: 14.5px;
  }
  .benefit-list {
    position: absolute; left: 37px; top: 220px; list-style: none;
    color: var(--ink); font-size: 11.6px; line-height: 16.2px;
  }
  .benefit-list li::before {
    content: ""; display: inline-block; width: 6px; height: 6px; border-radius: 50%;
    background: var(--green); margin-right: 5px; vertical-align: 1px;
  }
  .postcard--back .brand-mark {
    left: 18px; top: 300px; width: 112px;
    flex-direction: column; gap: 4px; white-space: normal;
    text-align: center; font-size: 16px; line-height: 18px;
  }
  .postcard--back .brand-mark__dot { width: 14px; height: 14px; }

  .contact-list {
    position: absolute; left: 140px; top: 295px; list-style: none;
    font-size: 14px; line-height: 20px; color: var(--ink);
  }
  .contact-list__label { font-family: "Oswald", sans-serif; font-weight: 600; font-size: 12.5px; }
  .contact-list__label--phone { color: var(--blue); }
  .contact-list__label--web { color: var(--pink); }
  .contact-list__label--mail { color: var(--orange); }

  .leaf-bursts {
    position: absolute; left: 450px; top: 310px; width: 168px; height: 52px;
    background: linear-gradient(90deg, rgba(252,194,0,.25), rgba(0,149,217,.25), rgba(124,192,42,.3));
    border-radius: 26px;
  }
  .thanks-band-text {
    position: absolute; left: 0; right: 0; top: 378px; text-align: center;
    font-family: "Oswald", sans-serif; font-weight: 500; color: var(--white);
    font-size: 13px;
  }
</style>
</head>
<body>
<div class="canvas">

  <section class="postcard postcard--front">
    <svg class="shape-layer" viewBox="0 0 618 412" aria-hidden="true">
      <path class="green-edge" fill="var(--green)" d="M0,98 C12,120 18,140 20,160 C24,190 48,205 56,225 C62,250 58,280 80,305 L95,412 L0,412 Z"/>
      <path class="gold-edge" fill="var(--gold)" d="M247,0 L257,40 L272,72 L292,92 L320,132 L336,172 L350,212 L352,242 L362,272 L380,302 L400,332 L410,372 L440,412 L618,412 L618,0 Z"/>
      <path class="blue-field" fill="var(--blue)" d="M255,0 L265,40 L280,70 L300,90 L330,130 L345,170 L360,210 L360,240 L370,270 L390,300 L410,330 L422,370 L455,412 L618,412 L618,0 Z"/>
      <path class="pink-banner" fill="var(--pink)" d="M316,45 L380,36 L470,32 L560,37 L618,40 L618,167 L560,166 L470,160 L380,168 L360,130 L330,90 L308,70 Z"/>
      <path class="swoosh" fill="none" stroke="var(--white)" stroke-width="3" stroke-linecap="round" d="M443,257 C490,251 545,251 592,253"/>
    </svg>
    <div class="brand-mark"><span class="brand-mark__dot"></span>Bright Lantern Youth</div>
    <div class="hero-photo" role="img" aria-label="Photo of a smiling child in a sun hat holding a cardboard box of donated clothes, framed by colourful leaf shapes"></div>
    <h1 class="headline-donate">DONATE</h1>
    <p class="headline-unwanted">YOUR UNWANTED<br>CLOTHING</p>
    <h2 class="headline-help">Help Children<br>in Need..!</h2>
    <p class="front-copy">Your clothing donations directly support Bright Lantern Youth providing meals and medical care for children in Honduras.</p>
  </section>

  <section class="postcard postcard--back">
    <svg class="shape-layer" viewBox="0 0 618 412" aria-hidden="true">
      <path class="pink-corner" fill="var(--pink)" d="M0,0 L72,0 C70,20 60,30 40,33 C22,36 22,55 0,56 Z"/>
      <path class="sky-field" fill="var(--light-blue)" d="M389,0 L618,0 L618,98 C590,90 560,110 540,115 C510,122 500,95 470,90 C440,86 420,60 410,40 C400,20 392,10 389,0 Z"/>
      <path class="thanks-band" fill="var(--green)" d="M0,370 C80,362 170,356 260,366 C340,376 420,362 490,356 C550,352 590,366 618,360 L618,412 L0,412 Z"/>
    </svg>
    <div class="stamp-box"></div>
    <div class="address-line address-line--1"></div>
    <div class="address-line address-line--2"></div>
    <div class="address-line address-line--3"></div>

    <h2 class="back-title">FREE Clothing Pickup<br>Service in Your Area!</h2>
    <p class="back-copy back-copy--intro">Have any unwanted, reusable clothing? Instead of letting it go to waste, donate it! At Bright Lantern Youth, we collect second-hand clothing, and the proceeds help fund our mission to provide essential meals and medical services to children in need in Honduras.</p>
    <p class="back-copy back-copy--impact">By scheduling a FREE pickup today, you can make a huge impact on the lives of children who rely on our support.</p>
    <h3 class="schedule-title">Schedule Your FREE Clothing Pickup!</h3>
    <ul class="benefit-list">
      <li>Accepting all types of reusable clothing.</li>
      <li>Fast and easy service–just schedule, and we'll handle the rest.</li>
      <li>Help make a difference with your donation!</li>
    </ul>

    <div class="brand-mark"><span class="brand-mark__dot"></span>Bright Lantern Youth</div>
    <ul class="contact-list">
      <li><span class="contact-list__label contact-list__label--phone">Call us at:</span> (555) 014-2290</li>
      <li><span class="contact-list__label contact-list__label--web">Visit our website:</span> www.brightlanternyouth.org</li>
      <li><span class="contact-list__label contact-list__label--mail">Email:</span> donate@brightlanternyouth.org</li>
    </ul>
    <div class="leaf-bursts" role="img" aria-label="Small decorative bursts of yellow, blue and green leaves"></div>
    <p class="thanks-band-text">Thank you for supporting Bright Lantern Youth and helping to make the world a better place for children in need!</p>
  </section>

</div>
</body>
</html>
```